Flyer Chorkonzert Frühlingsreigen Wolkenhüpfer
Zielgruppe
Wir sind ein gemischter Chor aus der Schweiz unsere Mitglieder sind zwischen 20 und 70 Jahre jung und singen Querbeet durch die Musik von Telmann bis Marrowind.
Weitere Infos www.wolkenhüpfer-chor.ch
Aufgabenstellung
Für unser Konzert mit dem Titel " Frühlingsreigen Wolkenhüpfer" brauchen wir für den Flyer ein Vorderseite Design. Das Konzertprogramm beinhaltet folgende Lieder:
Lanterna/ Varley, Silberner Nebel / Henk Morlitz, Ali di vento/ Lina,Ruth+Beni, Brunnmatt / Gleis,Under the lantern/ Gaukler von Lumm, Nowhere to hide/Marrowind, Winds of the bay/ trad. Irl.,Danse ma plume/trad CH,Never leave the harbour lights behind you/ Gareth Pim, Olas del mar/Tinfold, Paint your Window/Ray Binder.
Idealerweise nimmt das Design Bezug auf den Titel oder auf eines oder mehrere Lieder.
Format: A5 hoch
Text: "Frühlingsreigen Wolkenhüpfer"
Samstag 7. November 2015
17.00 Uhr, Singsaal Lärchenhalde, Uerikon / Stäfa
Sonntag 8. November 2015
17.00 Uhr Kornackersaal, Uetikon am See
Eintritt frei Kollekte

```html
<!DOCTYPE html>
<html lang="de">
<head>
<meta charset="utf-8">
<title>Frühlingsreigen Wolkenhüpfer – Flyer</title>
<link rel="stylesheet" href="https://fonts.googleapis.com/css2?family=Oswald:wght@400;500;700&display=swap">
<style>
  :root {
    --stage: #d9d9d9;
    --paper: #ffffff;
    --ink: #111111;
    --orange: #f3a52a;
    --song-grey: #9a9a9a;
    --faint: #ececec;
  }
  * { margin: 0; padding: 0; box-sizing: border-box; }
  html, body { width: 1200px; height: 705px; overflow: hidden; }
  body {
    background: var(--stage);
    font-family: "Oswald", "Arial Narrow", sans-serif;
    position: relative;
  }
  .flyer {
    position: absolute;
    left: 365px; top: 19px;
    width: 470px; height: 667px;
    background: var(--paper);
    overflow: hidden;
  }
  .backdrop-notes {
    position: absolute;
    left: 0; top: 360px; width: 470px; height: 307px;
    background: radial-gradient(ellipse at 40% 60%, var(--faint) 0%, rgba(236,236,236,0) 70%);
  }
  .title {
    position: absolute; left: 0; right: 0; top: 14px;
    text-align: center; text-transform: uppercase; line-height: 1;
    font-weight: 700;
  }
  .title-top {
    display: block; color: var(--ink);
    font-size: 62px; letter-spacing: -1px;
  }
  .title-bottom {
    display: block; color: var(--orange);
    font-size: 50px; margin-top: 4px;
  }
  .music-art {
    position: absolute; left: 0; top: 150px;
    width: 470px; height: 150px;
  }
  .ring {
    position: absolute; left: 30px; top: 255px;
    width: 386px; height: 386px;
    border: 3px solid var(--orange); border-radius: 50%;
  }
  .disc {
    position: absolute; left: 55px; top: 282px;
    width: 350px; height: 350px;
    background: var(--ink); border-radius: 50%;
    overflow: hidden; text-align: center; color: var(--paper);
    text-transform: uppercase;
  }
  .event { font-size: 16px; line-height: 1.15; font-weight: 500; }
  .event:first-child { margin-top: 18px; }
  .event .accent { color: var(--orange); }
  .divider {
    width: 230px; margin: 6px auto 4px;
    border-top: 2px dotted var(--paper);
  }
  .admission {
    margin-top: 6px; font-size: 14px; line-height: 17px; letter-spacing: 3px;
    color: var(--orange); font-weight: 400;
  }
  .admission-rule { border-top: 2px solid var(--orange); margin: 3px 0 4px; }
  .songs {
    color: var(--song-grey); font-size: 10px; line-height: 13px;
    font-weight: 500;
  }
</style>
</head>
<body>
  <article class="flyer">
    <div class="backdrop-notes" role="img" aria-label="Faint grey music staff with notes in the background"></div>
    <h1 class="title">
      <span class="title-top">Frühlingsreigen</span>
      <span class="title-bottom">Wolkenhüpfer</span>
    </h1>
    <svg class="music-art" viewBox="0 0 470 150" role="img" aria-label="Flowing orange and grey music staff with notes, a conductor and a choir in silhouette">
      <defs>
        <linearGradient id="staff-tone" x1="0" y1="0" x2="1" y2="0">
          <stop offset="0" stop-color="#f3a52a" stop-opacity="0.55"/>
          <stop offset="0.45" stop-color="#f3a52a" stop-opacity="0.25"/>
          <stop offset="0.6" stop-color="#777" stop-opacity="0.3"/>
          <stop offset="1" stop-color="#555" stop-opacity="0.5"/>
        </linearGradient>
      </defs>
      <path d="M0 70 C60 40 100 110 170 90 C240 70 280 110 340 80 C400 50 430 20 470 30 L470 55 C430 45 400 75 340 105 C280 135 240 95 170 115 C100 135 60 65 0 95 Z" fill="url(#staff-tone)"/>
      <rect x="195" y="35" width="80" height="115" rx="30" fill="#3a3a3a" opacity="0.85"/>
    </svg>
    <div class="ring"></div>
    <section class="disc">
      <p class="event">Samstag<br><span class="accent">7. November 2015</span><br>17.00 Uhr, Singsaal Lärchenhalde<br>Uerikon / Stäfa</p>
      <div class="divider"></div>
      <p class="event"><span class="accent">Sonntag 8</span> November 2015<br>17.00 Uhr Kornackersaal<br>Uetikon am See</p>
      <p class="admission">Eintritt frei Kollekte</p>
      <div class="admission-rule"></div>
      <p class="songs">Lanterna/ Varley, Silberner Nebel/ Henk Morlitz,<br>Ali di vento/ Lina,Ruth+Beni, Brunnmatt/ Gleis,<br>Under the lantern/ Gaukler von Lumm,<br>Nowhere to hide/ Marrowind, Winds of<br>the bay/ trad. Irl., Danse ma plume/<br>trad CH, Never leave the harbour<br>lights behind you/ Gareth Pim,<br>Olas del mar/ Tinfold, Paint<br>your Window/ Ray Binder</p>
    </section>
  </article>
</body>
</html>
```